Design business card using existing logo.

PLEASE DO NOT USE "RED WHITE & BLACK" color combo! Thank you.

Try different color combos such as:
- Vintage colors like brown, orange, gold, blue (not all together but a combo of 1 or 3
- Blue, w/ grey, or silver or white, Blue monochromatic can work as well.
- Use monochromatic variations on back (just an idea)

- Include full name, "Quillmarsh Records" on at least one side.

Target Market(s)

Teens

Industry/Entity Type

Business

Colors
3277b5
ffc214
f04a50
f78f20

```html
<!DOCTYPE html>
<html lang="en">
<head>
<meta charset="utf-8">
<title>Quillmarsh Records – Business Card</title>
<link href="https://fonts.googleapis.com/css2?family=Montserrat:wght@400;600;700&family=Lato:wght@400&display=swap" rel="stylesheet">
<style>
  :root {
    --backdrop: #6e5a45;
    --card-blue: #3277b5;
    --card-coral: #f04a50;
    --pattern-coral: #f2585d;
    --gold: #ffc214;
    --orange: #f78f20;
    --icon-red: #f04a50;
    --white: #ffffff;
    --divider: rgba(255,255,255,0.55);
  }
  * { margin: 0; padding: 0; box-sizing: border-box; }
  html, body { width: 900px; height: 1200px; overflow: hidden; }
  body { background: var(--backdrop); position: relative; font-family: "Lato", Arial, sans-serif; }

  .card {
    position: absolute; left: 82px; width: 733px; height: 429px;
    border-radius: 22px; overflow: hidden;
    box-shadow: 0 4px 10px rgba(0,0,0,0.35);
  }
  .card--front { top: 138px; background: var(--card-blue); }
  .card--back { top: 633px; background: var(--card-coral); }

  /* front */
  .brand-block {
    position: absolute; left: 146px; top: 142px; width: 162px;
    text-align: center; color: var(--white);
    font-family: "Montserrat", Arial, sans-serif; font-weight: 700;
    font-size: 17px; line-height: 1.25; letter-spacing: 0.5px;
  }
  .brand-block .brand-dot {
    display: block; width: 72px; height: 72px; border-radius: 50%;
    background: var(--gold); margin: 0 auto 14px;
  }
  .divider {
    position: absolute; left: 345px; top: 142px; width: 1px; height: 145px;
    background: var(--divider);
  }
  .identity { position: absolute; left: 380px; top: 138px; }
  .identity .person-name {
    font-family: "Montserrat", Arial, sans-serif; font-size: 25px;
    color: var(--white); letter-spacing: 0.3px; line-height: 1;
  }
  .identity .person-name strong { font-weight: 700; }
  .identity .person-name span { font-weight: 400; }
  .identity .person-role {
    font-family: "Montserrat", Arial, sans-serif; font-weight: 600;
    font-size: 15px; color: var(--gold); letter-spacing: 1px; margin-top: 6px;
  }
  .contact-list { list-style: none; margin-top: 14px; }
  .contact-list li {
    display: flex; align-items: center; height: 26.5px;
    font-size: 17px; color: var(--white);
  }
  .contact-list .icon {
    width: 24px; height: 24px; border-radius: 50%;
    background: var(--icon-red); border: 2px solid var(--orange);
    margin-right: 12px; display: flex; align-items: center; justify-content: center;
  }
  .contact-list svg { width: 12px; height: 12px; }
  .address {
    position: absolute; left: 0; right: 0; top: 371px; text-align: center;
    font-size: 15px; color: var(--white);
  }

  /* back */
  .pattern-field {
    position: absolute; inset: 0;
    background: linear-gradient(180deg, var(--pattern-coral), var(--card-coral));
  }
  .brand-center {
    position: absolute; left: 0; right: 0; top: 115px; text-align: center;
  }
  .brand-center .brand-dot {
    display: block; width: 150px; height: 150px; border-radius: 50%;
    background: var(--white); margin: 0 auto 36px;
  }
  .brand-center .brand-name {
    font-family: "Montserrat", Arial, sans-serif; font-weight: 600;
    font-size: 36px; color: var(--white); letter-spacing: 0.5px;
  }
</style>
</head>
<body>

<section class="card card--front">
  <div class="brand-block">
    <span class="brand-dot"></span>
    QUILLMARSH<br>RECORDS
  </div>
  <div class="divider"></div>
  <div class="identity">
    <div class="person-name"><strong>OWEN</strong> <span>PARRISH</span></div>
    <div class="person-role">MANAGING DIRECTOR</div>
    <ul class="contact-list">
      <li><span class="icon"><svg viewBox="0 0 12 12"><path d="M1 4 Q6 0 11 4 L9 5.5 L7.5 4 L4.5 4 L3 5.5 Z M3 6 H9 L10 10 H2 Z" fill="#fff"/></svg></span>27 10 555 0148</li>
      <li><span class="icon"><svg viewBox="0 0 12 12"><rect x="1" y="2.5" width="10" height="7" fill="#fff"/><path d="M1 2.5 L6 6.5 L11 2.5" fill="none" stroke="#f04a50" stroke-width="1"/></svg></span>owen@larchfield.com</li>
      <li><span class="icon"><svg viewBox="0 0 12 12"><circle cx="6" cy="6" r="5" fill="none" stroke="#fff" stroke-width="1.2"/><ellipse cx="6" cy="6" rx="2.2" ry="5" fill="none" stroke="#fff" stroke-width="1"/><path d="M1 6 H11" stroke="#fff" stroke-width="1"/></svg></span>www.larchfield.com</li>
    </ul>
  </div>
  <p class="address">42 Harbor Lane North, Suite 210, Dunmore Falls, NJ</p>
</section>

<section class="card card--back">
  <div class="pattern-field" role="img" aria-label="Repeating tone-on-tone brand pattern across the card"></div>
  <div class="brand-center">
    <span class="brand-dot"></span>
    <div class="brand-name">QUILLMARSH RECORDS</div>
  </div>
</section>

</body>
</html>
```